2-Page Flyer for the Information Session about the Tranquil Venture Course

This is a flyer to announce/advertise an evening Information Session about the Tranquil Venture Course. This Program aims at mindfully rethinking and redesigning work (and life) for people who feel stuck or not entirely satisfied with their work and/or life (please see draft flyer attached for more details). This Program is property of Brightfold Joy, a company that uses a combination of Mindfulness, Design, and Entrepreneurship to help people achieve greater happiness (in their work and lives).
Updates

Target Market(s)

People who feel stuck or not entirely satisfied with their work and/or life (please see draft flyer attached for more details)

Font styles to use
Serif
Sans Serif

Colors
ffffff
f37122
33a6d7
acd037

Requirements
Must have
• All of what I will say below is suggestive (I’m not a design expert), and I’m open to divert from it, if it makes sense and feels more interesting.
• I thought initially of a 2-page flyer (please see draft flyer attached). The first page could help people grasp the essence of the event quickly (in 1 or 2 minutes), and then, if they are interested/motivated, they would continue reading through page 2, which has more info about the Program in itself.
• Potential Structure
• Page 1
• . About the Information Session on the Tranquil Venture Course
• . Visible Date & Time, Contacts, Venue (and other relevant info)
• . About me (the facilitator)
• Page 2
• . About the Tranquil Venture Course
• I include a Powerpoint draft of the flyer with the content. The design is rudimentary and precarious from an aesthetics/organization point of view, and this is mainly where I need help (and maybe in other aspects too!).
• On the flyer, I would like to include:
• . A photo of myself (I attach 1 picture).
• . 1 or 2 beautiful-nature photos (cropped or full). One may have to do with looking at the sky, dreaming, and imagining a new work and life (2 photos with sky and clouds attached). The other has to do with walking the transformation journey (the photo with the person walking through the forest path).
• . brightfold joy logo or logos (there are two slightly different ones, that can be used for different purposes). For the first page, I would like the brightfold joy logo that has "brightfold joy" written on the bottom, with the saying "Stillness, Craft and Venture for Joy" beneath. This is the main logo. For the 2nd page, you can choose the logo that adapts better.
• - Where it says the "the way out is in" it would be great to have a similar font to the one I attach (see file "Font_the_way_out_is_in.png" and Ankecallig-fg.ttf
Nice to have
• In terms of colours, I would not divert much from the logo colours (and of course white and black). I would like the flyer to be quite white. Almost like fairy-tale white: the white horse, the white snow, the white of the stars, the white heaven. White could be the base colour. White means peace, tranquillity, calm contentment, a smile.
• And then use the other colours. The green of the mindfulness. The blue of the sky, the dreams. And the orange of the sun, the energy, the fire, the action. And maybe the black for text.
• Where it says the "the way out is in" it would be great to have a similar font to the one I attach (see file "Font_the_way_out_is_in".
• I would like this flyer to be a piece of art, in every possible way. Simple, beautiful, ease, light, peaceful, calm happy. Just like the Tranquil Venture Course and brightfold joy Company that I am creating intends to be. The mission of this Program and Company is to be a designer, a painter (a Picasso) of happier and more fulfilling human lives.
• I am very much looking forward to seeing your proposal(s).

```html
<!DOCTYPE html>
<html lang="en">
<head>
<meta charset="utf-8">
<title>Tranquil Venture Course – Free Information Session</title>
<link href="https://fonts.googleapis.com/css2?family=Jost:ital,wght@0,400;0,500;0,600;0,700;0,800;0,900;1,400;1,500&display=swap" rel="stylesheet">
<style>
  :root {
    --white: #ffffff;
    --paper: #fbfbfb;
    --backdrop: #eeeeee;
    --ink: #1a1a1a;
    --ink-soft: #333333;
    --grey: #666666;
    --orange: #e8843a;
    --orange-deep: #f37122;
    --blue: #33a6d7;
    --blue-band: #3f9fd8;
    --green: #acd037;
    --photo-dark: #3b4a5a;
    --photo-mid: #7d8fa0;
    --photo-skin: #c9a28c;
  }
  * { box-sizing: border-box; margin: 0; padding: 0; }
  html, body {
    width: 1200px; height: 1200px; overflow: hidden;
    background: var(--backdrop);
    font-family: "Jost", sans-serif;
    color: var(--ink);
  }
  .flyer {
    position: absolute; left: 197px; top: 30px;
    width: 806px; height: 1140px;
    background: var(--paper);
    box-shadow: 0 10px 40px rgba(0,0,0,.12);
    overflow: hidden;
  }
  .top-bands { position: absolute; left: 0; top: 0; width: 806px; height: 70px; }

  .brand { position: absolute; left: 44px; top: 78px; width: 170px; }
  .brand-mark { width: 74px; height: 74px; border-radius: 50%; background: var(--blue); margin-bottom: 14px; }
  .brand-name { font-size: 38px; font-weight: 400; line-height: .95; color: var(--orange-deep); }
  .brand-tagline { margin-top: 12px; font-size: 13px; line-height: 1.45; color: var(--grey); }

  .title {
    position: absolute; left: 232px; top: 84px; width: 560px;
    font-size: 60px; font-weight: 800; line-height: 1.08; letter-spacing: -0.5px;
    text-transform: uppercase; color: var(--ink);
  }

  .session { position: absolute; left: 46px; top: 318px; width: 180px; }
  .session-label { font-size: 21px; font-weight: 800; line-height: 1.2; text-transform: uppercase; }
  .session-details { list-style: none; margin-top: 20px; }
  .session-details li { display: flex; gap: 8px; font-size: 13.5px; line-height: 1.35; color: var(--ink-soft); margin-bottom: 14px; white-space: nowrap; }
  .session-details svg { flex: 0 0 16px; width: 16px; height: 16px; margin-top: 1px; }

  .intro { position: absolute; left: 232px; top: 318px; width: 530px; }
  .intro-lead { font-size: 18px; font-weight: 500; line-height: 1.38; color: var(--ink); }
  .section-heading { margin-top: 30px; font-size: 22px; font-weight: 700; }
  .section-rule { width: 30px; height: 3px; background: var(--blue); margin: 10px 0 18px; }
  .intro-body { font-size: 14.5px; line-height: 1.5; color: var(--ink-soft); }

  .facilitator-band {
    position: absolute; left: 24px; top: 612px; width: 782px; height: 396px;
    background: linear-gradient(90deg, var(--orange-deep), var(--orange));
  }
  .facilitator-photo {
    position: absolute; left: 32px; top: 570px; width: 176px; height: 414px;
    border-radius: 88px 88px 0 0;
    background: linear-gradient(180deg, var(--photo-skin) 0%, var(--photo-skin) 30%, var(--photo-mid) 42%, var(--photo-dark) 100%);
  }
  .facilitator { position: absolute; left: 232px; top: 636px; width: 540px; color: var(--white); }
  .facilitator-heading { font-size: 26px; font-weight: 700; }
  .facilitator-name { margin-top: 12px; font-size: 15px; font-weight: 600; }
  .facilitator-name em { font-weight: 400; }
  .facilitator-rule { width: 30px; height: 3px; background: var(--white); margin: 10px 0 14px; }
  .facilitator-bio { font-size: 13.4px; line-height: 1.42; }

  .profile-ribbon {
    position: absolute; left: 108px; top: 966px; width: 520px; height: 38px;
  }
  .profile-ribbon svg { position: absolute; inset: 0; }
  .profile-ribbon p {
    position: relative; display: flex; align-items: center; gap: 10px;
    height: 38px; padding-left: 28px; color: var(--white); font-size: 14px; font-weight: 600;
  }
  .profile-ribbon .dot { width: 18px; height: 18px; border-radius: 50%; background: var(--white); }
  .profile-ribbon .url { font-weight: 400; }

  .booking {
    position: absolute; left: 46px; top: 1060px; width: 730px;
    display: flex; align-items: center; gap: 14px; font-size: 15px; color: var(--ink);
  }
  .booking-label { font-size: 18px; font-weight: 700; margin-right: 8px; }
  .booking-arrow { color: var(--blue); font-size: 20px; font-weight: 600; margin-right: 6px; }
  .booking .chat-dot { width: 18px; height: 18px; border-radius: 50%; border: 2.5px solid var(--blue); }
  .booking .phone { font-weight: 600; margin-right: 28px; }
  .booking .email { font-weight: 600; }
  .booking svg { width: 22px; height: 18px; }
</style>
</head>
<body>
<article class="flyer">
  <svg class="top-bands" viewBox="0 0 806 70" aria-hidden="true">
    <polygon points="0,8 248,0 254,18 0,18" fill="var(--blue)"/>
    <polygon points="262,0 806,0 806,52 282,56" fill="var(--orange)"/>
  </svg>

  <header class="brand">
    <div class="brand-mark"></div>
    <p class="brand-name">brightfold<br>joy</p>
    <p class="brand-tagline">Stillness, Craft and<br>Venture for Joy</p>
  </header>

  <h1 class="title">Tranquil<br>Venture<br>Course</h1>

  <section class="session">
    <h2 class="session-label">Free Information Session</h2>
    <ul class="session-details">
      <li>
        <svg viewBox="0 0 16 16" aria-hidden="true"><rect x="1.5" y="3" width="13" height="11.5" fill="none" stroke="var(--orange)" stroke-width="1.4"/><line x1="1.5" y1="6.5" x2="14.5" y2="6.5" stroke="var(--orange)" stroke-width="1.4"/><line x1="5" y1="1" x2="5" y2="4" stroke="var(--orange)" stroke-width="1.4"/><line x1="11" y1="1" x2="11" y2="4" stroke="var(--orange)" stroke-width="1.4"/></svg>
        <span>Thursday,<br>5th September 2019</span>
      </li>
      <li>
        <svg viewBox="0 0 16 16" aria-hidden="true"><circle cx="8" cy="8" r="6.6" fill="none" stroke="var(--orange)" stroke-width="1.4"/><polyline points="8,4 8,8 11,9.5" fill="none" stroke="var(--orange)" stroke-width="1.4"/></svg>
        <span>19:30 to 21:00</span>
      </li>
      <li>
        <svg viewBox="0 0 16 16" aria-hidden="true"><path d="M8 15 C4 10 3 8 3 6 A5 5 0 0 1 13 6 C13 8 12 10 8 15Z" fill="none" stroke="var(--orange)" stroke-width="1.4"/><circle cx="8" cy="6" r="1.8" fill="none" stroke="var(--orange)" stroke-width="1.3"/></svg>
        <span>Lumen Coworking,<br>C/ Verdi 41, Barcelona</span>
      </li>
    </ul>
  </section>

  <section class="intro">
    <p class="intro-lead">The purpose of this free Information Session is to give you a real insight into the Tranquil Venture Course and how it can help you make the most of your professional and personal life.</p>
    <h2 class="section-heading">Who Can Come</h2>
    <div class="section-rule"></div>
    <p class="intro-body">Whether you come on your own, or with friends or family, you’ll be warmly welcomed. The session will take place on Thursday the 5th September 2019, from 19:30 to 21:00, at LUMEN Coworking. Please see information below to get in contact or to book a seat.</p>
  </section>

  <div class="facilitator-band"></div>
  <div class="facilitator-photo" role="img" aria-label="Portrait photo of the facilitator in a dark blazer and scarf"></div>

  <section class="facilitator">
    <h2 class="facilitator-heading">About Facilitator</h2>
    <p class="facilitator-name">Dr. Tomas Valen, <em>Visiting Research Fellow, University of Northmere</em></p>
    <div class="facilitator-rule"></div>
    <p class="facilitator-bio">Tomas joined the University of Northmere School of Management as a Lecturer in Entrepreneurship in 2015. He completed his PhD in Entrepreneurship at Kelvinbrook Business School in 2014, receiving the prestigious Academy of Enterprise Studies’ Harwell Doctoral Dissertation Award. He began his business career as a Production Engineer for Veltrix, and later as a Sales Engineer for Ostrand. After his MBA, he served as a Strategy Consultant for Douro Business School. Originally from Portugal, Tomas enjoys designing and launching new ideas, international communities, mindfulness retreats, and musical improvisation. He nurtures a close connection to Stillwater Hamlet Mindfulness Centre, where he has practiced and volunteered over 9 months. He has a broad experience of sharing the benefits of mindfulness with others.</p>
  </section>

  <div class="profile-ribbon">
    <svg viewBox="0 0 520 38" preserveAspectRatio="none" aria-hidden="true">
      <polygon points="8,0 520,0 512,38 0,38" fill="var(--blue-band)"/>
    </svg>
    <p>More about the facilitator: <span class="dot"></span> <span class="url">www.profilehub.net/in/tvalen</span></p>
  </div>

  <footer class="booking">
    <span class="booking-label">Information &amp; Booking</span>
    <span class="booking-arrow">›</span>
    <svg viewBox="0 0 22 18" aria-hidden="true"><rect x="1" y="3" width="13" height="12" rx="2" fill="var(--blue)"/><polygon points="15,9 21,4 21,14" fill="var(--blue)"/></svg>
    <span class="chat-dot"></span>
    <span class="phone">+34 611 482 305</span>
    <svg viewBox="0 0 22 18" aria-hidden="true"><rect x="1.5" y="3" width="19" height="13" fill="none" stroke="var(--blue)" stroke-width="1.8"/><polyline points="1.5,3 11,11 20.5,3" fill="none" stroke="var(--blue)" stroke-width="1.8"/></svg>
    <span class="email">info@brightfoldjoy.io</span>
  </footer>
</article>
</body>
</html>
```